Public Adjuster mailing campaign

We are public insurance adjusters. When people (the insured) are not being paid fairly on their insurance claim, we help them get paid all they are owed according to their coverage.We would like a post card mailer to send to homes that have been damaged by a recent tornado. I would like to say something like...Storm Damage?Is your insurance paying everything you are owed?You have rights!Get a FREE claim review!CALL NOW!972-954-6845ADJUSTER FOR THE INSUREDI would like to see a photo in the back ground of a damaged home. I would like a design on both sides of the post card.Colors I prefer are navy as a base color and white text ( or red text for the CALL NOW and the phone number.I would like the message to communicate I am a licensed public adjuster working for the insured and I can help them get what they are owed from the insurance company.

```html
<!DOCTYPE html>
<html lang="en">
<head>
<meta charset="utf-8">
<title>Storm Damage Postcard</title>
<link href="https://fonts.googleapis.com/css2?family=Lato:wght@400;700;900&family=Oswald:wght@500;700&display=swap" rel="stylesheet">
<style>
  :root {
    --navy: #1a4da3;
    --navy-deep: #163f8a;
    --yellow: #f5e21a;
    --ink: #222326;
    --charcoal: #333436;
    --red: #e0201f;
    --paper: #ffffff;
    --page: #e9e9ea;
  }
  * { margin: 0; padding: 0; box-sizing: border-box; }
  html, body { width: 902px; height: 1200px; overflow: hidden; background: var(--page); }
  body { position: relative; font-family: "Lato", sans-serif; color: var(--ink); }

  .card { position: absolute; left: 87px; width: 728px; overflow: hidden; box-shadow: 0 2px 6px rgba(0,0,0,.25); }
  .card-front { top: 58px; height: 522px; background: var(--navy); }
  .card-back { top: 609px; height: 524px; background: var(--paper); }
  .card svg.shapes { position: absolute; inset: 0; }

  .abs { position: absolute; white-space: nowrap; }

  .headline { right: 28px; top: 66px; font-family: "Oswald", sans-serif; font-weight: 700; font-size: 60px; line-height: 1; color: var(--ink); letter-spacing: .5px; }
  .headline .accent { color: var(--navy); }
  .question { right: 30px; top: 142px; text-align: right; font-weight: 700; font-size: 26.5px; line-height: 31px; color: var(--ink); }
  .rights { right: 40px; top: 216px; font-weight: 700; font-size: 19px; color: var(--navy); }
  .review { left: 296px; top: 272px; font-weight: 900; font-size: 24px; color: var(--yellow); }
  .call { left: 305px; top: 358px; font-weight: 700; font-size: 29px; color: var(--ink); }
  .call .phone { color: var(--red); margin-left: 18px; }
  .role { right: 40px; top: 420px; font-weight: 700; font-size: 23px; color: var(--ink); }

  .tab-title { left: 22px; top: 34px; font-weight: 700; font-size: 23px; color: var(--paper); }
  .about-text { left: 13px; top: 84px; width: 345px; white-space: normal; font-size: 12.4px; line-height: 15.6px; text-align: justify; color: var(--ink); }
  .offer { left: 25px; top: 268px; font-family: "Oswald", sans-serif; font-weight: 500; font-size: 19.5px; line-height: 30px; color: var(--paper); letter-spacing: .3px; }
  .visit { left: 38px; top: 385px; font-weight: 700; font-size: 14px; color: var(--paper); line-height: 22px; }
  .site { left: 37px; top: 410px; font-weight: 700; font-size: 14px; color: var(--paper); display: flex; align-items: center; gap: 4px; }
  .site .dot { width: 11px; height: 11px; border-radius: 50%; background: var(--yellow); display: inline-block; }
  .follow { left: 40px; top: 438px; font-weight: 700; font-size: 17px; color: var(--paper); display: flex; align-items: center; gap: 10px; }
  .follow .square { width: 14px; height: 14px; background: var(--paper); display: inline-block; }
</style>
</head>
<body>

<section class="card card-front">
  <svg class="shapes" width="728" height="522" viewBox="0 0 728 522">
    <defs>
      <linearGradient id="houseTone" x1="0" y1="0" x2="1" y2="1">
        <stop offset="0" stop-color="#eceef2"/>
        <stop offset=".55" stop-color="#d9d6d2"/>
        <stop offset="1" stop-color="#c9c3bc"/>
      </linearGradient>
      <radialGradient id="suitTone" cx=".55" cy=".5" r=".6">
        <stop offset="0" stop-color="#3c4a63"/>
        <stop offset="1" stop-color="#121a2a"/>
      </radialGradient>
    </defs>
    <path role="img" aria-label="Photo of a storm-damaged home with debris" d="M170 45 Q450 25 728 50 L728 448 Q400 490 87 428 Z" fill="url(#houseTone)"/>
    <path d="M300 42 Q520 22 728 35 L728 48 Q520 36 300 42 Z" fill="var(--yellow)"/>
    <path d="M87 428 Q400 490 728 448 L728 459 Q400 501 87 435 Z" fill="var(--yellow)"/>
    <circle cx="45" cy="185" r="252" fill="var(--navy-deep)"/>
    <circle cx="45" cy="185" r="242" fill="var(--yellow)"/>
    <circle cx="45" cy="185" r="235" fill="var(--navy)"/>
    <circle role="img" aria-label="Photo of a businessman's cupped hands holding a house and family symbol" cx="42" cy="182" r="228" fill="url(#suitTone)"/>
    <path d="M265 258 L680 258 L710 318 L285 318 Z" fill="#1b1b1c"/>
    <path d="M285 318 L710 318 L712 324 L287 324 Z" fill="var(--yellow)"/>
    <rect x="270" y="348" width="480" height="52" rx="8" fill="#f2f2f2"/>
  </svg>

  <h1 class="abs headline">Storm <span class="accent">Damage?</span></h1>
  <p class="abs question">IS YOUR INSURANCE PAYING<br>EVERYTHING YOU ARE OWED?</p>
  <p class="abs rights">YOU HAVE RIGHTS!</p>
  <p class="abs review">GET A FREE CLAIM REVIEW!</p>
  <p class="abs call">CALL NOW!<span class="phone">641-387-2290</span></p>
  <p class="abs role">ADJUSTER FOR THE INSURED</p>
</section>

<section class="card card-back">
  <svg class="shapes" width="728" height="524" viewBox="0 0 728 524">
    <path d="M262 0 C380 40 420 150 415 300" fill="none" stroke="var(--navy)" stroke-width="9"/>
    <path d="M0 28 L158 28 L180 68 L0 68 Z" fill="var(--charcoal)"/>
    <path d="M0 68 L180 68 L182 73 L0 73 Z" fill="var(--yellow)"/>
    <rect x="0" y="240" width="405" height="86" fill="var(--charcoal)"/>
    <path d="M0 340 Q180 358 330 378 L400 378 L400 470 L0 470 Z" fill="var(--navy)"/>
    <path d="M0 333 Q180 352 330 372 L330 379 Q180 360 0 341 Z" fill="var(--yellow)"/>
    <circle cx="351" cy="400" r="92" fill="var(--yellow)"/>
    <circle cx="351" cy="400" r="86" fill="var(--navy)"/>
    <circle role="img" aria-label="Photo of hands working with a calculator, charts and paperwork" cx="351" cy="400" r="82" fill="#c9d6e6"/>
    <rect x="617" y="58" width="83" height="104" fill="none" stroke="#9a9a9a" stroke-width="1"/>
    <line x1="445" y1="235" x2="700" y2="235" stroke="#8a8a8a" stroke-width="1"/>
    <line x1="445" y1="281" x2="700" y2="281" stroke="#8a8a8a" stroke-width="1"/>
    <line x1="445" y1="324" x2="700" y2="324" stroke="#8a8a8a" stroke-width="1"/>
  </svg>

  <h2 class="abs tab-title">About Us</h2>
  <p class="abs about-text">Lorem ipsum dolor sit amet, consectetuer adipiscing elit. Aenean commodo ligula eget dolor. Aenean massa. Cum sociis natoque penatibus et magnis dis parturient montes, nascetur ridiculus mus. Donec quam felis, ultricies nec, pellentesque eu, pretium quis, sem. Nulla consequat massa quis enim. Donec pede justo, fringilla vel, aliquet nec, vulputate eget, arcu. In enim justo, rhoncus ut, imperdiet a, venenatis vitae, justo. Nullam dictum felis eu pede mollis pretium. Integer tincidunt. Cras dapibus.</p>
  <p class="abs offer">We will evaluate your claim for FREE</p>
  <p class="abs visit">Visit Us at:</p>
  <p class="abs site"><span class="dot"></span>www.yourwebsitename.com</p>
  <p class="abs follow">Follow us on <span class="square"></span><span>Friendbook</span></p>
</section>

</body>
</html>
```